Orbell Consulting- executive coaching business

looking for business card design for a newly started coaching business.
specialising in Exective coaching, Leadership, NLP and Motivation.
Looking for a simple, classy design using the existing logo attached and colour themes that complement the logo.
No red or orange in the business card design please.

Target Market(s)

Defence and Veteran community

Industry/Entity Type

Life Coaching

Contact Information for Business Card

looking for business cards for newly started coaching business.
specialising in Exective Coaching, Leadership, NLP and Motivation

Font styles to use
Serif
Script

Colors
0556a4
3176b5
86cfc6
33b8a4

Requirements
Must have
• Logo
• Email address- Jess@orbellconsulting.com.au
• Contact number
• Services provided - Executive Coaching, Leadership, NLP and Motivational Mapping.
Nice to have
• Same colours as logo
Should not have
• Red or orange

```html
<!DOCTYPE html>
<html lang="en">
<head>
<meta charset="utf-8">
<title>Orbell Consulting – Business Card</title>
<link rel="stylesheet" href="https://fonts.googleapis.com/css2?family=Source+Sans+3:ital,wght@0,400;0,600;1,400&display=swap">
<style>
  :root {
    --page: #9b9b9b;
    --card-front: #f4f4f4;
    --brand-blue: #1763ab;
    --name-blue: #1f5fa6;
    --brand-green: #2a9d5c;
    --ink: #4a4a4a;
    --muted: #8f8f8f;
    --white: #ffffff;
    --back-blue: #1766ad;
  }
  * { box-sizing: border-box; margin: 0; padding: 0; }
  html, body { width: 1105px; height: 1200px; overflow: hidden; }
  body {
    background: var(--page);
    font-family: "Source Sans 3", "Myriad Pro", Arial, sans-serif;
    position: relative;
  }
  .card {
    position: absolute;
    left: 182px;
    width: 746px;
    height: 427px;
    overflow: hidden;
  }
  .card--front { top: 119px; background: var(--card-front); }
  .card--back { top: 637px; background: var(--back-blue); }

  /* front */
  .brand {
    position: absolute;
    right: 38px;
    top: 33px;
    width: 340px;
    height: 150px;
  }
  .brand__mark {
    position: absolute;
    left: 178px;
    top: 0;
    width: 96px; height: 96px;
    border: 3px solid var(--muted);
    border-radius: 50%;
  }
  .brand__name {
    position: absolute;
    right: 0;
    top: 108px;
    font-size: 33px;
    font-weight: 600;
    color: var(--brand-blue);
    letter-spacing: 0.5px;
    white-space: nowrap;
  }
  .person__bar {
    position: absolute;
    left: 0; top: 222px;
    width: 11px; height: 55px;
    background: var(--brand-blue);
  }
  .person__name {
    position: absolute;
    left: 39px; top: 224px;
    font-size: 27px;
    font-weight: 600;
    color: var(--name-blue);
  }
  .person__role {
    position: absolute;
    left: 39px; top: 256px;
    font-size: 20px;
    font-weight: 400;
    color: var(--brand-green);
  }
  .rule {
    position: absolute;
    left: 179px; top: 276px;
    width: 529px; height: 1.5px;
    background: var(--name-blue);
  }
  .contact {
    position: absolute;
    left: 39px; top: 295px;
    list-style: none;
    font-size: 19px;
    color: var(--ink);
  }
  .contact li {
    display: flex;
    align-items: center;
    height: 29px;
  }
  .contact svg { width: 18px; height: 18px; margin-right: 9px; fill: var(--name-blue); flex: none; }
  .services {
    position: absolute;
    right: 38px; top: 296px;
    text-align: right;
  }
  .services__title {
    font-size: 23px;
    font-weight: 600;
    color: var(--name-blue);
    line-height: 30px;
  }
  .services__line {
    font-size: 19px;
    font-style: italic;
    color: var(--ink);
    line-height: 27px;
  }
  .services__dot { color: var(--name-blue); font-style: normal; }
  .band {
    position: absolute;
    left: 0; bottom: 0;
    width: 746px; height: 21px;
  }

  /* back */
  .back-mark {
    position: absolute;
    left: 303px; top: 62px;
    width: 140px; height: 140px;
    border: 4px solid var(--white);
    border-radius: 50%;
  }
  .back-name {
    position: absolute;
    left: 0; top: 226px;
    width: 746px;
    text-align: center;
    font-size: 30px;
    font-weight: 600;
    color: var(--white);
    letter-spacing: 0.5px;
    line-height: 38px;
  }
  .back-services {
    position: absolute;
    left: 0; top: 331px;
    width: 746px;
    text-align: center;
    color: var(--white);
    font-size: 21px;
    line-height: 28px;
  }
  .back-services strong { font-weight: 600; }
  .back-services em { font-style: italic; }
</style>
</head>
<body>

<section class="card card--front" aria-label="Business card front">
  <div class="brand">
    <span class="brand__mark" aria-hidden="true"></span>
    <span class="brand__name">ORBELL CONSULTING</span>
  </div>

  <span class="person__bar" aria-hidden="true"></span>
  <h1 class="person__name">Daniel Carter</h1>
  <p class="person__role">CEO/Founder</p>
  <span class="rule" aria-hidden="true"></span>

  <ul class="contact">
    <li>
      <svg viewBox="0 0 24 24" aria-hidden="true"><path d="M6.6 10.8a15.1 15.1 0 0 0 6.6 6.6l2.2-2.2a1 1 0 0 1 1-.25 11.4 11.4 0 0 0 3.6.57 1 1 0 0 1 1 1V20a1 1 0 0 1-1 1A17 17 0 0 1 3 4a1 1 0 0 1 1-1h3.5a1 1 0 0 1 1 1c0 1.25.2 2.45.57 3.57a1 1 0 0 1-.25 1z"/></svg>
      612 555 0148
    </li>
    <li>
      <svg viewBox="0 0 24 24" aria-hidden="true"><path d="M2 5h20v14H2z M3.5 6.5 12 12.5l8.5-6z" fill-rule="evenodd"/></svg>
      Jess@orbellconsulting.com.au
    </li>
    <li>
      <svg viewBox="0 0 24 24" aria-hidden="true"><path d="M12 2a10 10 0 1 0 0 20 10 10 0 0 0 0-20zm0 2a8 8 0 0 1 6.9 4H15c-.4-1.4-1-2.7-1.8-3.8A8 8 0 0 1 12 4zM4.3 10h3.4a16 16 0 0 0 0 4H4.3a8 8 0 0 1 0-4zm5.4 0h4.6a14 14 0 0 1 0 4H9.7a14 14 0 0 1 0-4zm6.6 0h3.4a8 8 0 0 1 0 4h-3.4a16 16 0 0 0 0-4zM5.1 16h3.9c.4 1.4 1 2.7 1.8 3.8A8 8 0 0 1 5.1 16zm5.9 0h2c-.3 1.1-.8 2.2-1 2.9-.3-.7-.7-1.8-1-2.9zm4 0h3.9a8 8 0 0 1-5.7 3.8c.8-1.1 1.4-2.4 1.8-3.8zM5.1 8a8 8 0 0 1 5.7-3.8C10 5.3 9.4 6.6 9 8zm5.9 0c.3-1.1.7-2.2 1-2.9.3.7.7 1.8 1 2.9z"/></svg>
      www.orbellconsulting.com.au
    </li>
  </ul>

  <div class="services">
    <h2 class="services__title">Services provided</h2>
    <p class="services__line">Executive Coaching <span class="services__dot">•</span> Leadership <span class="services__dot">•</span></p>
    <p class="services__line">NLP &amp; Motivational Mapping <span class="services__dot">•</span></p>
  </div>

  <svg class="band" viewBox="0 0 746 21" preserveAspectRatio="none" aria-hidden="true">
    <polygon points="0,0 488,0 482,21 0,21" fill="var(--brand-blue)"/>
    <polygon points="494,0 746,0 746,21 488,21" fill="var(--brand-green)"/>
  </svg>
</section>

<section class="card card--back" aria-label="Business card back">
  <span class="back-mark" aria-hidden="true"></span>
  <p class="back-name">ORBELL CONSULTING</p>
  <p class="back-services">
    <strong>Services provided:</strong> <em>Executive Coaching</em><br>
    <em>Leadership • NLP and Motivational Mapping</em>
  </p>
</section>

</body>
</html>
```